International printing supplier needs full stationery design

We would like a full stationery design to line up with our new logo and branding.
(In order to symbolise our responsiveness and fast service in the logo, we used an arrow as the accent on the “e“ in the company name.)

What designs we are looking for:
-font to be used in all documentation
-letterhead
-business card
-envelope TC4 (229x324 mm) and LC6 (114x162 mm)
-fax header
-email header
-smaller product labels (69x36mm and 104x73mm)
-bigger product label (A5)
-logo for email signature
-rubber stamp pattern
-flag pattern

Our company (Bóra) is B2B and is based in Central Europe. We operate in the printing press industry supplying press rooms with inks, additives and professional advice.

The design should thus communicate professionalism, responsiveness and swiftness.

Our current logo is attached and our main branding is based around the following colours:
Dark grey: RAL 7016
Orange: RAL 2004 (close to PMS 1655)
Light grey: RAL 9006 (or Pantone Cool Gray 10)

The Look and Feel Slider below should aid anyone in terms of what we imagined the stationery to look like.

Requirements
Must have
• Logo should be clearly visible on all elements.

The designed or chosen font should match the logo's font and it should be easy to read.

The bigger product label must have an area coloured orange, which needs to contain (maximum 4) industry standard hazard symbols by law. Therefore, these legal constraints need to be included in the design of the product labels. It would be ideal if they could be integrated with the company's orange colour scheme and the rest of the stationery.
Nice to have
• The logo and slogan (Friss lendülettel!®) should be presented together on all of the proposed designs.

The arrow in the logo would be an ideal symbol to use across the different elements.

The designs should be similar for all the different stationery elements, communicating a clear image and professionalism.
Should not have
• Expensive or impractical solutions in elements of the stationery (i.e. cut-outs, metallic font colours, special materials etc.) should be avoided.

Too many colours on each of the elements of the stationery are not needed, keep it simple.

```html
<!DOCTYPE html>
<html lang="hu">
<head>
<meta charset="utf-8">
<title>Bóra – Stationery</title>
<link href="https://fonts.googleapis.com/css2?family=Montserrat:wght@400;500;600;700&family=Pinyon+Script&display=swap" rel="stylesheet">
<style>
  :root {
    --orange: #b8461d;
    --dark-grey: #4b4b4d;
    --paper: #f3f3f3;
    --backdrop: #d8d8d8;
    --text-grey: #6a6a6a;
    --rule-grey: #9a9a9a;
  }
  * { box-sizing: border-box; margin: 0; padding: 0; }
  html, body { width: 1200px; height: 840px; overflow: hidden; }
  body {
    position: relative;
    background: var(--backdrop);
    font-family: "Montserrat", sans-serif;
    color: var(--text-grey);
  }
  .sheet { position: absolute; background: var(--paper); box-shadow: 0 2px 6px rgba(0,0,0,.12); }
  .wordmark {
    position: absolute;
    font-family: "Montserrat", sans-serif;
    font-weight: 700;
    color: var(--orange);
    letter-spacing: .02em;
    line-height: 1;
  }
  .slogan { position: absolute; font-weight: 500; color: var(--text-grey); white-space: nowrap; }
  .edge-mark { position: absolute; left: 0; background: var(--orange); }
  .contact {
    position: absolute;
    border-left: 1px solid var(--rule-grey);
    padding-left: 7px;
    line-height: 1.45;
    color: var(--text-grey);
  }
  .contact b { color: var(--orange); font-weight: 600; }

  /* Letterhead */
  .letterhead { left: 60px; top: 120px; width: 380px; height: 537px; }
  .letterhead .wordmark { right: 40px; top: 38px; font-size: 34px; }
  .letterhead .slogan { left: 34px; top: 106px; font-size: 12px; }
  .letterhead .edge-mark { top: 106px; width: 6px; height: 14px; }
  .letterhead .contact { left: 34px; bottom: 34px; font-size: 6.5px; }

  /* Company profile folder */
  .folder {
    left: 470px; top: 120px; width: 300px; height: 424px;
    background: var(--dark-grey);
    border-bottom: 6px solid var(--orange);
    border-right: 6px solid var(--orange);
  }
  .folder .wordmark { right: 32px; top: 30px; font-size: 22px; }
  .folder .slogan { left: 28px; top: 34px; font-size: 9px; color: #e2e2e2; }
  .folder .title {
    position: absolute; right: 32px; top: 170px; text-align: right;
    color: #fff; font-weight: 700; font-size: 20px; line-height: 1.15;
  }
  .folder .title small {
    display: block; font-size: 9px; font-weight: 500; letter-spacing: .08em; color: #d8d8d8;
  }

  /* Envelope DL */
  .envelope { left: 800px; top: 120px; width: 340px; height: 170px; }
  .envelope .wordmark { left: 150px; top: 36px; font-size: 24px; }
  .envelope .slogan { left: 24px; top: 84px; font-size: 10px; }
  .envelope .edge-mark { top: 84px; width: 5px; height: 12px; }
  .envelope .contact { left: 24px; bottom: 22px; font-size: 5.5px; }

  /* Compliments slip */
  .compliments { left: 800px; top: 320px; width: 340px; height: 160px; }
  .compliments .wordmark { right: 26px; top: 22px; font-size: 24px; }
  .compliments .slogan { left: 24px; top: 50px; font-size: 10px; }
  .compliments .edge-mark { top: 50px; width: 5px; height: 12px; }
  .compliments .contact { left: 24px; top: 74px; font-size: 5.5px; }
  .compliments .greeting {
    position: absolute; right: 24px; bottom: 30px;
    font-family: "Pinyon Script", cursive; font-size: 26px; color: var(--text-grey);
  }
  .compliments .greeting span { color: var(--orange); }

  /* Business cards */
  .card { width: 250px; height: 145px; }
  .card-front { left: 470px; top: 590px; background: var(--dark-grey); color: #e0e0e0; }
  .card-front .wordmark { right: 22px; top: 20px; font-size: 20px; }
  .card-front .slogan { left: 18px; top: 24px; font-size: 9px; color: #e6e6e6; }
  .card-front .contact { left: 18px; top: 56px; font-size: 5.5px; color: #d0d0d0; border-color: #8a8a8a; }
  .card-front .person { position: absolute; right: 22px; top: 60px; text-align: right; }
  .card-front .person .name { font-size: 7px; font-weight: 700; letter-spacing: .06em; color: #fff; }
  .card-front .person .role { font-size: 5.5px; color: var(--orange); font-weight: 600; }
  .card-back { left: 800px; top: 590px; background: var(--orange); }
  .card-back .wordmark { left: 0; right: 0; top: 58px; text-align: center; font-size: 28px; color: #fff; }
</style>
</head>
<body>

<section class="sheet letterhead" aria-label="Letterhead">
  <div class="wordmark">bóra</div>
  <span class="edge-mark"></span>
  <div class="slogan">Friss lendülettel!®</div>
  <address class="contact">
    14 Kikötő utca<br>Budapest, 1095 Hungary<br>
    <b>T:</b> +36 1 555 0142<br><b>F:</b> +36 1 555 0143<br><b>M:</b> +36 30 555 0188<br>
    <b>E:</b> info@borainks.eu<br><b>W:</b> www.borainks.eu<br>
    Bóra Ltd is registered in Hungary<br>Reg. no. 01-09-555123
  </address>
</section>

<section class="sheet folder" aria-label="Company profile folder">
  <div class="slogan">Friss lendülettel!®</div>
  <div class="wordmark">bóra</div>
  <h1 class="title">Leading<br>Innovations<small>COMPANY PROFILE</small></h1>
</section>

<section class="sheet envelope" aria-label="Envelope">
  <div class="wordmark">bóra</div>
  <span class="edge-mark"></span>
  <div class="slogan">Friss lendülettel!®</div>
  <address class="contact">14 Kikötő utca<br>Budapest, 1095 Hungary</address>
</section>

<section class="sheet compliments" aria-label="Compliments slip">
  <div class="wordmark">bóra</div>
  <span class="edge-mark"></span>
  <div class="slogan">Friss lendülettel!®</div>
  <address class="contact">
    14 Kikötő utca<br>Budapest, 1095 Hungary<br>
    <b>T:</b> +36 1 555 0142<br><b>F:</b> +36 1 555 0143<br>
    <b>E:</b> info@borainks.eu<br><b>W:</b> www.borainks.eu<br>
    Bóra Ltd is registered in Hungary. Reg. no. 01-09-555123
  </address>
  <div class="greeting"><span>With</span> Compliments</div>
</section>

<section class="sheet card card-front" aria-label="Business card front">
  <div class="slogan">Friss lendülettel!®</div>
  <div class="wordmark">bóra</div>
  <address class="contact">
    14 Kikötő utca<br>Budapest, 1095 Hungary<br>
    <b>T:</b> +36 1 555 0142<br><b>M:</b> +36 30 555 0188<br>
    <b>E:</b> info@borainks.eu<br><b>W:</b> www.borainks.eu
  </address>
  <div class="person">
    <div class="name">NORA KELEMEN</div>
    <div class="role">Sales Manager</div>
  </div>
</section>

<section class="sheet card card-back" aria-label="Business card back">
  <div class="wordmark">bóra</div>
</section>

</body>
</html>
```